Tidewell Shuck-new seafood raw bar restaurant menu

We are a Local Seafood & Raw Bar restaurant that is looking to open in 3 months. I need-Dinner Menu Design, Happy Hour Menu, Cocktail Menu, Brunch Menu, Lunch Menu. I'd like to have you start w/ the dinner menu first then whomever I choose will also do the rest of my menus. The OYSTERDECK by Finnhook menu is the direction im going for as far as font organization. Id like you to give us our own personal touch. Ive also provided a mock menu that a local designer started that can't finish due to timing.

Target Market(s)

mid to high end casual seafood restaurant

Industry/Entity Type

restaurant

Font styles to use
Serif
Sans Serif

Colors
0054AA
0677BA
7BADD7
CADEEF
E8F1F8
0094D4
00A9DD
6FCCEA
C7EBF8
E9F6FB
00AB8E
00BBA5
67D7C9
C6EFE9
E9F9F6

Requirements
Must have
• 11" x 14" size

```html
<!DOCTYPE html>
<html lang="en">
<head>
<meta charset="UTF-8">
<title>Tidewell Shuck — Dinner Menu</title>
<link rel="stylesheet" href="https://fonts.googleapis.com/css2?family=Josefin+Sans:wght@700&family=Montserrat:wght@300;400;500&display=swap">
<style>
  :root {
    --ink: #1d4a9a;
    --ink-soft: #2b5aa8;
    --teal: #62c3cb;
    --panel: #d3ebee;
    --paper: #eef4f3;
    --rule: #8fd2d8;
    --art: #dce7ee;
    --art-edge: #cfdde8;
  }
  * { margin: 0; padding: 0; box-sizing: border-box; }
  html, body { width: 1200px; height: 878px; overflow: hidden; background: #ffffff; }
  .canvas { position: relative; width: 1200px; height: 878px; background: #ffffff; font-family: "Montserrat", sans-serif; color: var(--ink); }
  .sheet { position: absolute; left: 62px; top: 54px; width: 1076px; height: 771px; background: linear-gradient(160deg, #f3f6f5 0%, var(--paper) 55%, #e6f1f1 100%); overflow: hidden; }
  .frame { position: absolute; left: 89px; top: 79px; width: 1022px; height: 717px; border: 1px solid var(--rule); }
  .art { position: absolute; border-radius: 14px; background: linear-gradient(150deg, var(--art) 0%, var(--art-edge) 100%); }

  .brand { position: absolute; left: 178px; top: 101px; width: 176px; height: 176px; border: 6px solid var(--ink); border-radius: 50%; display: flex; align-items: center; justify-content: center; text-align: center; }
  .brand-name { font-family: "Josefin Sans", sans-serif; font-weight: 700; font-size: 24px; line-height: 1.15; letter-spacing: 1px; color: var(--ink); }

  .title { position: absolute; left: 100px; width: 332px; text-align: center; font-family: "Josefin Sans", sans-serif; font-weight: 700; font-size: 34px; letter-spacing: 1.5px; line-height: 1; color: var(--ink); }
  .ornament { position: absolute; left: 229px; top: 429px; width: 74px; height: 10px; border-radius: 5px; background: var(--teal); opacity: 0.55; }
  .menu-pill { position: absolute; left: 195px; top: 483px; width: 142px; height: 46px; border-radius: 23px; background: var(--teal); color: #fff; font-size: 21px; font-weight: 400; letter-spacing: 1px; display: flex; align-items: center; justify-content: center; }

  .panel { position: absolute; background: var(--panel); border-radius: 4px; }
  .heading { position: absolute; text-align: center; font-family: "Josefin Sans", sans-serif; font-weight: 700; font-size: 26px; letter-spacing: 2.5px; line-height: 1.2; color: var(--ink); }

  .grilled-box { position: absolute; left: 448px; top: 636px; width: 305px; height: 135px; border: 3px solid var(--teal); border-radius: 4px; }
  .grilled-box .cover { position: absolute; background: var(--paper); }

  .item { position: absolute; }
  .item-row { display: flex; align-items: baseline; font-size: 12.5px; font-weight: 500; letter-spacing: 0.2px; color: var(--ink); }
  .item-name { white-space: nowrap; }
  .leader { flex: 1; border-bottom: 1.5px dotted var(--ink-soft); margin: 0 8px; transform: translateY(-3px); }
  .price { white-space: nowrap; }
  .item-desc { margin-top: 6px; font-size: 9.5px; font-weight: 300; line-height: 16px; color: var(--ink-soft); }
</style>
</head>
<body>
<div class="canvas">
  <div class="sheet"></div>
  <div class="frame"></div>

  <div class="art" role="img" aria-label="Line sketch of an oyster shell" style="left:62px;top:54px;width:90px;height:82px;border-radius:0 0 14px 0;"></div>
  <div class="art" role="img" aria-label="Line sketch of a salmon steak" style="left:662px;top:54px;width:98px;height:80px;border-radius:0 0 14px 14px;"></div>
  <div class="art" role="img" aria-label="Line sketch of a fish" style="left:1045px;top:54px;width:93px;height:108px;border-radius:0 0 0 14px;"></div>
  <div class="art" role="img" aria-label="Line sketch of an octopus tentacle" style="left:62px;top:367px;width:60px;height:112px;border-radius:0 14px 14px 0;"></div>
  <div class="art" role="img" aria-label="Line sketch of a shrimp" style="left:1043px;top:383px;width:95px;height:122px;border-radius:14px 0 0 14px;"></div>
  <div class="art" role="img" aria-label="Line sketch of a crab" style="left:109px;top:564px;width:290px;height:223px;"></div>
  <div class="art" role="img" aria-label="Line sketch of a lobster" style="left:1003px;top:740px;width:135px;height:85px;border-radius:14px 0 0 0;"></div>

  <div class="brand"><div class="brand-name">TIDEWELL<br>SHUCK</div></div>

  <div class="title" style="top:312px;">LOCAL SEAFOOD</div>
  <div class="title" style="top:360px;">&amp; RAW BAR</div>

  <div class="ornament" role="img" aria-label="Small wave ornament"></div>

  <div class="menu-pill">MENU</div>

  <!-- Smaller -->
  <div class="panel" style="left:447px;top:103px;width:307px;height:481px;"></div>
  <div class="heading" style="left:447px;top:123px;width:307px;">SMALLER</div>

  <div class="item" style="left:465px;top:182px;width:272px;">
    <div class="item-row"><span class="item-name">SHRIMP AND GRITS</span><span class="leader"></span><span class="price">8 $</span></div>
    <div class="item-desc">Local andouille, roasted peppers, garlic, shallot, charred tomato</div>
  </div>
  <div class="item" style="left:465px;top:248px;width:272px;">
    <div class="item-row"><span class="item-name">CRAB MAC’N CHEESE</span><span class="leader"></span><span class="price">10 $</span></div>
    <div class="item-desc">Cheddar, fontina, cotija, local pasta shells</div>
  </div>
  <div class="item" style="left:465px;top:298px;width:272px;">
    <div class="item-row"><span class="item-name">SHRIMP AND GRITS</span><span class="leader"></span><span class="price">7 $</span></div>
    <div class="item-desc">Local andouille, roasted peppers, garlic, shallot, charred tomato</div>
  </div>
  <div class="item" style="left:465px;top:363px;width:272px;">
    <div class="item-row"><span class="item-name">SHRIMP REMOULADE</span><span class="leader"></span><span class="price">12 $</span></div>
    <div class="item-desc" style="margin-top:2px;">Avocado, fried green tomato</div>
  </div>
  <div class="item" style="left:465px;top:410px;width:272px;">
    <div class="item-row"><span class="item-name">SHRIMP AND GRITS</span><span class="leader"></span><span class="price">8 $</span></div>
    <div class="item-desc">Local andouille, roasted peppers, garlic, shallot, charred tomato</div>
  </div>
  <div class="item" style="left:465px;top:472px;width:272px;">
    <div class="item-row"><span class="item-name">CRAB MAC’N CHEESE</span><span class="leader"></span><span class="price">10 $</span></div>
    <div class="item-desc">Cheddar, fontina, cotija, local pasta shells</div>
  </div>
  <div class="item" style="left:465px;top:525px;width:272px;">
    <div class="item-row"><span class="item-name">CRAB MAC’N CHEESE</span><span class="leader"></span><span class="price">10 $</span></div>
    <div class="item-desc">Cheddar, fontina, cotija, local pasta shells</div>
  </div>

  <!-- Simply grilled fish -->
  <div class="grilled-box">
    <div class="cover" style="left:14px;top:-4px;width:270px;height:6px;"></div>
    <div class="cover" style="left:34px;bottom:-4px;width:230px;height:6px;"></div>
  </div>
  <div class="heading" style="left:448px;top:624px;width:305px;">SIMPLY GRILLED<br>FISH</div>
  <div class="item" style="left:465px;top:702px;width:272px;">
    <div class="item-row"><span class="item-name">SHRIMP AND GRITS</span><span class="leader"></span><span class="price">8 $</span></div>
    <div class="item-desc">Local andouille, roasted peppers, garlic, shallot, charred tomato</div>
  </div>
  <div class="art" role="img" aria-label="Line sketch of a whole fish" style="left:489px;top:756px;width:227px;height:62px;"></div>

  <!-- Kids menu -->
  <div class="heading" style="left:800px;top:123px;width:272px;">KIDS MENU</div>
  <div class="item" style="left:802px;top:182px;width:270px;">
    <div class="item-row"><span class="item-name">CHICKEN TENDERS</span><span class="leader"></span><span class="price">8 $</span></div>
    <div class="item-desc">Local andouille, roasted peppers, garlic, shallot, charred tomato</div>
  </div>
  <div class="item" style="left:802px;top:248px;width:270px;">
    <div class="item-row"><span class="item-name">CRAB MAC’N CHEESE</span><span class="leader"></span><span class="price">10 $</span></div>
    <div class="item-desc">Cheddar, fontina, cotija, local pasta shells</div>
  </div>
  <div class="item" style="left:802px;top:298px;width:270px;">
    <div class="item-row"><span class="item-name">FRIED FISH</span><span class="leader" style="margin-left:56px;"></span><span class="price">7 $</span></div>
    <div class="item-desc">Local andouille, roasted peppers, garlic, shallot, charred tomato</div>
  </div>
  <div class="item" style="left:802px;top:363px;width:236px;">
    <div class="item-row"><span class="item-name">FRIED SHRIMP</span><span class="leader" style="margin-left:36px;"></span><span class="price">7 $</span></div>
    <div class="item-desc">Local andouille, roasted peppers, garlic, shallot, charred tomato</div>
  </div>

  <!-- Signatures -->
  <div class="panel" style="left:786px;top:444px;width:307px;height:327px;"></div>
  <div class="heading" style="left:786px;top:473px;width:307px;">SIGNATURES</div>
  <div class="item" style="left:805px;top:532px;width:270px;">
    <div class="item-row"><span class="item-name">CLAM LINGUINI</span><span class="leader" style="margin-left:30px;"></span><span class="price">8 $</span></div>
    <div class="item-desc">Local andouille, roasted peppers, garlic, shallot, charred tomato</div>
  </div>
  <div class="item" style="left:805px;top:598px;width:270px;">
    <div class="item-row"><span class="item-name">VEGETABLE GNOCCHI</span><span class="leader"></span><span class="price">10 $</span></div>
    <div class="item-desc">Cheddar, fontina, cotija, local pasta shells</div>
  </div>
  <div class="item" style="left:805px;top:648px;width:270px;">
    <div class="item-row"><span class="item-name">PAN SEARED SCALLOPS</span><span class="leader"></span><span class="price">7 $</span></div>
    <div class="item-desc">Local andouille, roasted peppers, garlic, shallot, charred tomato</div>
  </div>
  <div class="item" style="left:805px;top:713px;width:270px;">
    <div class="item-row"><span class="item-name">HALIBUT GUMBOE</span><span class="leader" style="margin-left:22px;"></span><span class="price">12 $</span></div>
    <div class="item-desc" style="margin-top:2px;">Avocado, fried green tomato</div>
  </div>
</div>
</body>
</html>
```